Hello,
We’re looking for a new WordPress website for Gather Your Light, our company offering unique well-being retreats and workshops.
We currently have a website online (you can consult it : www.gatheryourlight.ch), but we now need to build a new site on WordPress — more flexible, more intuitive to manage, and better aligned with our evolving needs.

What we’re looking for:
A new userfriendly WordPress site, with:
Inspiring, elegant, and modern design
Smooth user experience on desktop and mobile
Innovative design proposals – we want to be inspired !
SEO best practices
Respect of our existing color palette
The final website will need to be set up on our existing hosting provider (details can be shared later)

Pages to Include:
- Home
- Our Story
- Our Stays - with links to 5 individual pages, each describing one of our stays in detail.
- Activities – with potential links to individual descriptive pages
- Agenda
- Our Charter
- The Team
- Contact
- Blog

Required Features:
- Space for photos and videos
- Sections for testimonials and press articles
- Blog/article layout with strong readability
- Easy-to-update backend for future content
- Newsletter sign-up (pop-up and in footer)
- Additional pop-up on/off
- “Request info” buttons
- “Booking request” buttons
- Integration of our 4 pillars - Breathe · Feel · Connect · Experience - in the design (They’re currently in the footer, but we’re open to creative suggestions)

Who we are :
Gather Your Light offers well-being and personal growth stays but with a very different spirit.
We’re not a classic wellness brand. Our approach is professional, joyful, and grounded.
We create spaces where people can take a real break — breathe, slow down, and reconnect with themselves.
During our stays, people are welcomed like friends:
with warmth, respect, and no pressure.
Each program combines practices like breathwork, movement, creativity, coaching, and massages in a relaxed, beautiful setting of the French Alps.
What makes us different:
A friendly and down-to-earth atmosphere
A wide mix of activities.
A mix of inner work and simple pleasures
Private rooms, nourishing food, and shared moments
Time to talk, to laugh, to walk, or just be silent together - and feel free to be yourself
Our guests come to pause.
They leave feeling lighter, aligned, and full of life

```html
<!DOCTYPE html>
<html lang="en">
<head>
<meta charset="utf-8">
<title>Gather Your Light – Well-being Stays</title>
<link href="https://fonts.googleapis.com/css2?family=Josefin+Sans:wght@600;700&family=Roboto:ital,wght@0,400;0,500;0,700;1,400&display=swap" rel="stylesheet">
<style>
:root{
  --navy:#1b3a93;
  --navy-deep:#0b2470;
  --teal:#5cbfba;
  --teal-light:#9fdcd7;
  --ink:#2b2b2b;
  --muted:#6b6f78;
  --white:#ffffff;
}
*{box-sizing:border-box;margin:0;padding:0}
html,body{width:1200px;height:3972px;overflow:hidden}
body{position:relative;font-family:"Roboto",Arial,sans-serif;color:var(--ink);background:var(--white)}
.abs{position:absolute}
.heading{font-family:"Josefin Sans",Arial,sans-serif;font-weight:700;letter-spacing:1px;text-transform:uppercase}
.heading .navy{color:var(--navy)}
.heading .teal{color:var(--teal)}
.btn{position:absolute;display:flex;align-items:center;justify-content:center;border-radius:30px;font:700 13px "Roboto",Arial,sans-serif;text-transform:uppercase;text-decoration:none}
.btn-teal{background:var(--teal);color:var(--white);border-left:4px solid var(--navy)}
.btn-outline{background:var(--white);color:var(--navy);border:2px solid var(--navy)}

/* header */
.brand{left:143px;top:20px;font:700 36px "Josefin Sans",Arial,sans-serif;color:var(--navy);letter-spacing:2px}
.brand-sub{left:145px;top:66px;font:500 12px "Roboto",Arial,sans-serif;color:var(--teal);letter-spacing:12px}
.nav{left:143px;top:108px;width:1057px;height:51px;background:var(--navy)}
.nav a{position:absolute;top:17px;font:700 13px "Roboto",Arial,sans-serif;color:var(--white);text-decoration:none;text-transform:uppercase}
.nav .active{left:0;top:0;width:96px;height:51px;border-radius:26px;background:var(--teal);display:flex;align-items:center;justify-content:center}

/* hero */
.hero{left:0;top:159px;width:1200px;height:580px;background:linear-gradient(100deg,#e7eef4 0%,#dfe8ef 40%,#c9d3dc 62%,#d3a27a 78%,#c88a60 92%)}
.hero-title{left:143px;top:318px;font-size:52px;line-height:46px}
.hero-title span{display:block}
.hero-sub{left:143px;top:472px;font:500 20px "Roboto",Arial,sans-serif;color:#222}
.dot{position:absolute;top:658px;width:9px;height:9px;border-radius:50%;background:#9aa3ad}
.dot.on{width:14px;height:14px;top:656px;background:none;border:3px solid var(--teal)}

/* pillars */
.pillar{position:absolute;top:740px;height:230px;border-radius:28px;display:flex;flex-direction:column;align-items:center;color:var(--white)}
.pillar.teal{background:linear-gradient(180deg,#9fdcd5 0%,#5cbfba 60%,#7fd0ca 100%)}
.pillar.navy{background:linear-gradient(180deg,#2f74c4 0%,#163d93 55%,#0b2470 100%)}
.pillar svg{margin-top:34px}
.pillar h3{margin-top:18px;font:700 21px "Josefin Sans",Arial,sans-serif;letter-spacing:1.5px}

/* who */
.who{left:0;top:975px;width:1200px;height:592px;background:linear-gradient(90deg,#ffffff 0%,#ffffff 50%,#fbeee2 80%,#f2e3d4 100%)}
.who-ring{left:145px;top:1068px;width:394px;height:394px;border-radius:50%;border:16px solid var(--navy);border-right-color:transparent}
.who-photo{left:178px;top:1100px;width:330px;height:330px;border-radius:50%;background:linear-gradient(120deg,#bfd4e0,#e8eef2 45%,#8ea7b7)}
.who-title{left:600px;top:1082px;font-size:46px}
.who-text{left:600px;top:1146px;width:455px;font-size:15px;line-height:30px;color:#555;text-align:justify}

/* different */
.diff{left:0;top:1567px;width:1200px;height:572px;background:linear-gradient(180deg,#d3eeec 0%,#e6f5f4 50%,#f4fafa 100%)}
.section-title{width:1200px;left:0;text-align:center;font-size:46px}
.feature{position:absolute;top:1782px;width:260px;text-align:center}
.feature .ring{margin:0 auto;width:156px;height:156px;border-radius:50%;border:3px solid var(--teal);background:var(--white);display:flex;align-items:center;justify-content:center}
.feature .ring.hot{border:9px solid var(--teal)}
.feature .inner{width:136px;height:136px;border-radius:50%;border:3px solid var(--navy);display:flex;align-items:center;justify-content:center}
.feature p{margin-top:22px;font:500 18px/27px "Roboto",Arial,sans-serif;color:#2a2a2a}
.arrow{position:absolute;width:44px;height:44px;border-radius:50%;border:2px solid #8a9099;display:flex;align-items:center;justify-content:center}

/* articles */
.featured{left:143px;top:2376px;width:455px;height:489px;border-radius:30px;background:linear-gradient(160deg,#cfc6b2 0%,#9f9a83 35%,#6d6a5c 70%,#2f2e2a 100%);overflow:hidden}
.featured .frame{position:absolute;left:14px;top:14px;right:14px;bottom:14px;border:2px solid rgba(255,255,255,.7);border-radius:24px}
.date{position:absolute;width:56px;height:56px;border-radius:8px;overflow:hidden;text-align:center;color:var(--white);font-weight:700}
.date .m{background:var(--navy);height:22px;font-size:12px;line-height:22px}
.date .y{background:var(--teal);height:34px;font-size:17px;line-height:32px}
.post h4{position:absolute;font:700 16px "Roboto",Arial,sans-serif;color:var(--navy);text-transform:uppercase}
.post p{position:absolute;width:300px;font-size:12px;line-height:24px;color:#777}
.divider{position:absolute;left:606px;width:449px;height:1px;background:#d9dde3}

/* testimonials */
.testi{left:0;top:2976px;width:1200px;height:506px;background:linear-gradient(180deg,#62c0bc 0%,#3ea7a6 55%,#237f86 100%)}
.quote{left:251px;top:3214px;width:700px;text-align:center;font:italic 18px/29px "Roboto",Arial,sans-serif;color:var(--white)}

/* footer */
.footer{left:0;top:3482px;width:1200px;height:490px;background:linear-gradient(180deg,#17358f 0%,#1d45a6 60%,#2c63c6 100%)}
.fline{position:absolute;left:143px;width:912px;height:1px;background:rgba(255,255,255,.3)}
.fnav a{position:absolute;top:3656px;font:700 14px "Roboto",Arial,sans-serif;color:var(--white);text-decoration:none}
.contact{position:absolute;display:flex;align-items:center;gap:12px;color:var(--white);font-size:14px;line-height:24px}
.ico{width:34px;height:34px;border-radius:50%;border:2px solid var(--white);display:flex;align-items:center;justify-content:center;flex-shrink:0}
.social{position:absolute;top:3893px;width:32px;height:32px;border-radius:50%;background:var(--white);border:3px solid #2a6fd0}
</style>
</head>
<body>

<!-- header -->
<div class="abs brand">GATHER</div>
<div class="abs brand-sub">YOUR LIGHT</div>
<a class="btn btn-teal" style="left:674px;top:26px;width:166px;height:43px">Request info</a>
<a class="btn btn-outline" style="left:854px;top:26px;width:200px;height:43px">Book an appointment</a>

<nav class="abs nav">
  <a class="active" href="#">Home</a>
  <a href="#" style="left:118px">Our Story</a>
  <a href="#" style="left:227px">Our Stays</a>
  <a href="#" style="left:335px">Activities</a>
  <a href="#" style="left:441px">Agenda</a>
  <a href="#" style="left:529px">Our Charter</a>
  <a href="#" style="left:656px">The Team</a>
  <a href="#" style="left:758px">Contact</a>
  <a href="#" style="left:853px">Blog</a>
</nav>

<!-- hero -->
<div class="abs hero" role="img" aria-label="Photo of a woman breathing in fresh air by a lake in soft morning light"></div>
<h1 class="abs heading hero-title"><span class="navy">Welcome to</span><span class="teal">Gather Your Light</span></h1>
<p class="abs hero-sub">A down to earth and joyful experience,in a beautiful place</p>
<a class="btn btn-teal" style="left:143px;top:538px;width:170px;height:43px">Request info</a>
<a class="btn btn-outline" style="left:325px;top:538px;width:202px;height:43px">Book an appointment</a>
<span class="dot" style="left:144px"></span>
<span class="dot" style="left:166px"></span>
<span class="dot on" style="left:184px"></span>
<span class="dot" style="left:209px"></span>

<!-- pillars -->
<div class="pillar teal" style="left:-20px;width:315px">
  <svg width="96" height="96" viewBox="0 0 96 96" fill="none" stroke="#fff" stroke-width="3" stroke-linecap="round"><circle cx="40" cy="30" r="16"/><path d="M30 46 L26 88 M50 46 L56 88"/><path d="M64 26 h14 M66 34 h18 M64 42 h12"/></svg>
  <h3>BREATHE</h3>
</div>
<div class="pillar navy" style="left:295px;width:306px">
  <svg width="96" height="96" viewBox="0 0 96 96" fill="none" stroke="#fff" stroke-width="3" stroke-linecap="round"><circle cx="48" cy="28" r="13"/><path d="M22 86 C22 58 74 58 74 86 Z"/><path d="M48 62 l-7 -7 a5 5 0 0 1 7 -5 a5 5 0 0 1 7 5 z"/></svg>
  <h3>FEEL</h3>
</div>
<div class="pillar teal" style="left:601px;width:304px">
  <svg width="96" height="96" viewBox="0 0 96 96" fill="none" stroke="#fff" stroke-width="3"><circle cx="48" cy="48" r="38"/><path d="M20 30 L60 20 L78 56 L40 76 Z M20 30 L78 56 M60 20 L40 76"/></svg>
  <h3>CONNECT</h3>
</div>
<div class="pillar navy" style="left:905px;width:315px">
  <svg width="96" height="96" viewBox="0 0 96 96" fill="none" stroke="#fff" stroke-width="3"><rect x="10" y="10" width="76" height="76" rx="28"/><circle cx="48" cy="40" r="10"/><path d="M30 72 C30 54 66 54 66 72"/></svg>
  <h3>EXPERIENCE</h3>
</div>

<!-- who we are -->
<div class="abs who"></div>
<div class="abs who-ring"></div>
<div class="abs who-photo" role="img" aria-label="Photo of a woman with closed eyes taking a calm deep breath"></div>
<h2 class="abs heading who-title"><span class="navy">Who we </span><span class="teal">are</span></h2>
<p class="abs who-text">Gather Your Light offers well-being and personal growth stays but with a very different spirit. We’re not a classic wellness brand. Our approach is professional, joyful, and grounded. We create spaces where people can take a real break — breathe, slow down, and reconnect with themselves. During our stays, people are welcomed like friends: with warmth, respect, and no pressure. Each program combines practices like breathwork, movement, creativity, coaching, and massages in a relaxed, beautiful setting of the French Alps.</p>
<a class="btn btn-teal" style="left:600px;top:1414px;width:168px;height:43px">Read more</a>

<!-- what makes us different -->
<div class="abs diff"></div>
<h2 class="abs heading section-title" style="top:1668px"><span class="navy">What makes </span><span class="teal">us different</span></h2>
<div class="arrow" style="left:83px;top:1838px"><svg width="14" height="20" viewBox="0 0 14 20" fill="none" stroke="#555" stroke-width="2"><path d="M11 2 L3 10 L11 18"/></svg></div>
<div class="arrow" style="left:1071px;top:1838px"><svg width="14" height="20" viewBox="0 0 14 20" fill="none" stroke="#555" stroke-width="2"><path d="M3 2 L11 10 L3 18"/></svg></div>

<div class="feature" style="left:94px">
  <div class="ring"><div class="inner"><svg width="70" height="70" viewBox="0 0 70 70" fill="none" stroke="var(--navy)" stroke-width="3"><path d="M35 62 L10 36 a14 14 0 0 1 25 -18 a14 14 0 0 1 25 18 Z"/></svg></div></div>
  <p>A friendly and<br>down-to-earth<br>atmosphere</p>
</div>
<div class="feature" style="left:328px">
  <div class="ring hot"><div class="inner" style="border-color:var(--teal);width:124px;height:124px"><svg width="60" height="70" viewBox="0 0 60 70" fill="none" stroke="var(--navy)" stroke-width="3" stroke-linecap="round"><circle cx="32" cy="10" r="6"/><path d="M30 20 L26 42 L16 64 M26 42 L38 64 M30 20 L42 8"/></svg></div></div>
  <p>A wide mix of<br>activities.</p>
</div>
<div class="feature" style="left:572px">
  <div class="ring"><div class="inner"><svg width="80" height="70" viewBox="0 0 80 70" fill="none" stroke="var(--navy)" stroke-width="3" stroke-linecap="round"><path d="M40 34 L28 22 a8 8 0 0 1 12 -10 a8 8 0 0 1 12 10 Z"/><path d="M6 30 L16 56 L34 58 M74 30 L64 56 L46 58"/></svg></div></div>
  <p>A mix of inner work<br>and simple pleasures</p>
</div>
<div class="feature" style="left:821px">
  <div class="ring"><div class="inner"><svg width="80" height="70" viewBox="0 0 80 70" fill="none" stroke="var(--navy)" stroke-width="3"><rect x="12" y="18" width="22" height="40" rx="3"/><circle cx="52" cy="44" r="14"/><path d="M12 28 h22"/></svg></div></div>
  <p>Private rooms, nourishing<br>food, &amp; shared moments</p>
</div>

<!-- latest articles -->
<h2 class="abs heading section-title" style="top:2254px"><span class="navy">Latest </span><span class="teal">articles</span></h2>

<article class="abs featured" role="img" aria-label="Video still of a woman with closed eyes surrounded by soft foliage">
  <div class="frame"></div>
  <svg class="abs" style="left:198px;top:172px" width="56" height="56" viewBox="0 0 56 56"><circle cx="28" cy="28" r="25" fill="#fff" stroke="var(--navy)" stroke-width="4"/><circle cx="28" cy="28" r="16" fill="var(--navy)"/><path d="M23 19 L36 28 L23 37 Z" fill="#fff"/></svg>
  <div class="date" style="left:40px;top:350px"><div class="m">JULY</div><div class="y">2025</div></div>
  <h4 class="abs" style="left:119px;top:348px;font:700 16px Roboto,Arial,sans-serif;color:#fff">SED UT PERSPICIATIS UNDE</h4>
  <p class="abs" style="left:119px;top:380px;width:300px;font-size:12px;line-height:24px;color:#fff">Nemo enim ipsam voluptatem quia voluptas sit aspernatur aut odit aut fugit, sed quia consequuntur magni dolores eos qui ratione voluptatem</p>
</article>

<div class="post">
  <div class="date" style="left:665px;top:2405px"><div class="m">JULY</div><div class="y">2025</div></div>
  <h4 style="left:744px;top:2400px">Sed ut perspiciatis unde</h4>
  <p style="left:744px;top:2432px">Nemo enim ipsam voluptatem quia voluptas sit aspernatur aut odit aut fugit, sed quia consequuntur magni dolores eos qui ratione voluptatem</p>
</div>
<div class="divider" style="top:2529px"></div>
<div class="post">
  <div class="date" style="left:665px;top:2557px"><div class="m">JULY</div><div class="y">2025</div></div>
  <h4 style="left:744px;top:2552px">Sed ut perspiciatis unde</h4>
  <p style="left:744px;top:2584px">Nemo enim ipsam voluptatem quia voluptas sit aspernatur aut odit aut fugit, sed quia consequuntur magni dolores eos qui ratione voluptatem</p>
</div>
<div class="divider" style="top:2683px"></div>
<div class="post">
  <div class="date" style="left:665px;top:2715px"><div class="m">JULY</div><div class="y">2025</div></div>
  <h4 style="left:744px;top:2710px">Sed ut perspiciatis unde</h4>
  <p style="left:744px;top:2742px">Nemo enim ipsam voluptatem quia voluptas sit aspernatur aut odit aut fugit, sed quia consequuntur magni dolores eos qui ratione voluptatem</p>
</div>
<div class="divider" style="top:2837px"></div>

<!-- testimonials -->
<section class="abs testi" role="img" aria-label="Background photo of a woman in a sun hat on a lakeside pier with palm trees"></section>
<h2 class="abs heading section-title" style="top:3058px;color:#fff">Customer testimonials</h2>
<svg class="abs" style="left:578px;top:3148px" width="44" height="44" viewBox="0 0 44 44" fill="none" stroke="#fff" stroke-width="2.5"><circle cx="22" cy="22" r="20"/><path d="M15 26 v-4 a5 5 0 0 1 5 -5 M15 26 h4 v-4 h-4 M25 26 v-4 a5 5 0 0 1 5 -5 M25 26 h4 v-4 h-4"/></svg>
<div class="arrow" style="left:83px;top:3208px;border-color:#fff"><svg width="14" height="20" viewBox="0 0 14 20" fill="none" stroke="#fff" stroke-width="2"><path d="M11 2 L3 10 L11 18"/></svg></div>
<div class="arrow" style="left:1071px;top:3208px;border-color:#fff"><svg width="14" height="20" viewBox="0 0 14 20" fill="none" stroke="#fff" stroke-width="2"><path d="M3 2 L11 10 L3 18"/></svg></div>
<blockquote class="abs quote">“Nemo enim ipsam voluptatem quia voluptas sit aspernatur aut odit aut fugit, sed quia consequuntur magni dolores eos qui ratione voluquia voluptas sit aspernatur aut odit aut fugit, sed quia consequuntur magni dolores eos qui raquia voluptas sit aspernatur aut odit aut fugit, sed quia consequuntur magni dolores eos qui raptatem ”</blockquote>
<p class="abs" style="left:0;width:1200px;top:3346px;text-align:center;font:500 18px Roboto,Arial,sans-serif;color:#fff">-Anna Reyes,Customer</p>
<svg class="abs" style="left:550px;top:3377px" width="100" height="20" viewBox="0 0 100 20" fill="#fff"><g id="star"><path d="M10 1 L12.6 7 L19 7.4 L14 11.6 L15.6 18 L10 14.5 L4.4 18 L6 11.6 L1 7.4 L7.4 7 Z"/></g><use href="#star" x="20"/><use href="#star" x="40"/><use href="#star" x="60"/><use href="#star" x="80"/></svg>

<!-- footer -->
<footer class="abs footer"></footer>
<h3 class="abs" style="left:174px;top:3540px;font:500 22px Roboto,Arial,sans-serif;color:#fff">SIGN UP TO OUR NEWSLETTER</h3>
<div class="abs" style="left:527px;top:3531px;width:346px;height:42px;border-radius:22px;background:#fff;padding-left:26px;line-height:42px;font-size:13px;color:#333">Enter Email</div>
<a class="btn" style="left:887px;top:3531px;width:137px;height:42px;background:var(--teal);color:#fff">Sign up</a>
<div class="fline" style="top:3616px"></div>
<nav class="fnav">
  <a href="#" style="left:166px">HOME</a>
  <a href="#" style="left:242px">OUR STORY</a>
  <a href="#" style="left:353px">OUR STAYS</a>
  <a href="#" style="left:463px">ACTIVITIES</a>
  <a href="#" style="left:570px">AGENDA</a>
  <a href="#" style="left:662px">OUR CHARTER</a>
  <a href="#" style="left:794px">THE TEAM</a>
  <a href="#" style="left:898px">CONTACT</a>
  <a href="#" style="left:996px">BLOG</a>
</nav>
<div class="contact" style="left:247px;top:3708px">
  <span class="ico"><svg width="16" height="16" viewBox="0 0 16 16" fill="none" stroke="#fff" stroke-width="2"><path d="M8 15 C3 9 3 7 3 6 a5 5 0 0 1 10 0 c0 1 0 3 -5 9 Z"/><circle cx="8" cy="6" r="1.6"/></svg></span>
  <span>Chemin du Lac 14<br>Building B2, CH - 1260 Nyon</span>
</div>
<div class="contact" style="left:535px;top:3716px">
  <span class="ico" style="background:var(--teal);border-color:var(--teal)"><svg width="16" height="16" viewBox="0 0 16 16" fill="#fff"><path d="M3 1 L6 1 L7 5 L5 6.5 C6 9 7 10 9.5 11 L11 9 L15 10 L15 13 C15 14 14 15 13 15 C6 15 1 10 1 3 C1 2 2 1 3 1 Z"/></svg></span>
  <span style="font-weight:700">+41 58 200 41 72</span>
</div>
<div class="contact" style="left:744px;top:3716px">
  <span class="ico"><svg width="16" height="12" viewBox="0 0 16 12" fill="none" stroke="#fff" stroke-width="1.8"><rect x="1" y="1" width="14" height="10" rx="1"/><path d="M1 2 L8 7 L15 2"/></svg></span>
  <span>info@gatheryourlight.ch</span>
</div>
<div class="fline" style="top:3801px"></div>
<p class="abs" style="left:0;width:1200px;top:3849px;text-align:center;font-size:14px;color:#fff">© 2025 Gather Your Light - All Rights Reserved &nbsp;| &nbsp;Privacy Policy &nbsp;| &nbsp;Terms of Use</p>
<span class="social" style="left:500px"></span>
<span class="social" style="left:542px"></span>
<span class="social" style="left:584px"></span>
<span class="social" style="left:626px"></span>
<span class="social" style="left:668px"></span>

</body>
</html>
```